Willowbend Pharmacy Business Cards

I need a business card design and or template. Needs to convey a softer feel along with health and wellness. Please see attached logo and color scheme.

Industry/Entity Type

Pharmacy

Colors

Designer to choose colors to be used in the design.

Requirements
Must have
• I've added a second NEW colored logo I think I am going to go with the blue green logo.
• Needs to have the colors and feel of the logo attached.
• Darrel Quimby
• Pharmacy Manager
• willowbendpharmacy.example

```html
<!DOCTYPE html>
<html lang="en">
<head>
<meta charset="utf-8">
<title>Willowbend Pharmacy – Business Cards</title>
<link rel="stylesheet" href="https://fonts.googleapis.com/css2?family=Open+Sans:wght@400;600;700&display=swap">
<style>
  :root {
    --backdrop: #e8e5e1;
    --card: #ffffff;
    --ink: #4a4d50;
    --brand-grey: #5b6064;
    --brand-blue: #2fa3dc;
    --brand-green: #8cc43f;
  }
  * { margin: 0; padding: 0; box-sizing: border-box; }
  html, body { width: 1200px; height: 1000px; overflow: hidden; }
  body {
    background: var(--backdrop);
    font-family: "Open Sans", Arial, sans-serif;
    color: var(--ink);
    position: relative;
  }
  .card {
    position: absolute;
    left: 266px;
    width: 666px;
    height: 397px;
    background: var(--card);
    border-radius: 22px;
    overflow: hidden;
    box-shadow: 0 4px 14px rgba(0,0,0,0.18);
  }
  .card--front { top: 74px; }
  .card--back { top: 533px; }

  .brand {
    position: absolute;
    display: flex;
    align-items: center;
    gap: 14px;
    color: var(--brand-grey);
    font-weight: 600;
    letter-spacing: -0.5px;
    white-space: nowrap;
  }
  .brand__dot {
    display: block;
    border-radius: 50%;
    background: var(--brand-green);
    flex: none;
  }
  .card--front .brand { left: 118px; top: 170px; font-size: 40px; }
  .card--front .brand__dot { width: 52px; height: 52px; }
  .card--back .brand { right: 32px; top: 78px; font-size: 34px; }
  .card--back .brand__dot { width: 44px; height: 44px; }

  .person { position: absolute; left: 33px; top: 197px; }
  .person__name {
    color: var(--brand-blue);
    font-weight: 700;
    font-size: 21px;
    letter-spacing: 0.2px;
    line-height: 26px;
  }
  .person__title { font-size: 15.5px; line-height: 22px; }

  .contact { position: absolute; left: 335px; top: 190px; font-size: 15.5px; line-height: 21px; }
  .contact__address { margin-bottom: 6px; }
  .contact__row { display: flex; align-items: center; gap: 6px; line-height: 22px; }
  .contact__icon { width: 15px; height: 13px; flex: none; fill: var(--brand-green); }

  .footer-band {
    position: absolute;
    left: 0;
    bottom: 0;
    width: 666px;
    height: 72px;
    background: linear-gradient(180deg, var(--brand-blue) 0%, var(--brand-green) 45%, var(--brand-green) 100%);
  }
</style>
</head>
<body>
  <section class="card card--front" aria-label="Card front">
    <div class="brand"><span class="brand__dot"></span>Willowbend Pharmacy</div>
  </section>

  <section class="card card--back" aria-label="Card back">
    <div class="brand"><span class="brand__dot"></span>Willowbend Pharmacy</div>

    <div class="person">
      <p class="person__name">DARREL QUIMBY</p>
      <p class="person__title">Pharmacy Manager</p>
    </div>

    <div class="contact">
      <p class="contact__address">118 Linden Grove Ave, Suite 4<br>Maplebrook Ontario K0L</p>
      <p class="contact__row">
        <svg class="contact__icon" viewBox="0 0 16 14" aria-hidden="true"><path d="M1 5c0-3 3-4 7-4s7 1 7 4l-3 1-1-2H5L4 6 1 5zm3 2h8l2 6H2l2-6zm4 1.5a2 2 0 1 0 0 4 2 2 0 0 0 0-4z"/></svg>
        555-014-2297 ext. 118
      </p>
      <p class="contact__row">
        <svg class="contact__icon" viewBox="0 0 16 14" aria-hidden="true"><path d="M1 2h14v1L8 8 1 3zm0 3 7 5 7-5v7H1z"/></svg>
        Darrel@willowbendpharmacy.example
      </p>
      <p class="contact__row">
        <svg class="contact__icon" viewBox="0 0 16 14" aria-hidden="true"><path d="M7 0a7 7 0 1 0 0 14A7 7 0 0 0 7 0zm0 2a5 5 0 0 1 0 10A5 5 0 0 1 7 2z"/></svg>
        www.willowbendpharmacy.example
      </p>
    </div>

    <div class="footer-band" role="img" aria-label="Decorative blue and green footer artwork"></div>
  </section>
</body>
</html>
```